Modern business card for triathlon training business in Australia

We need a business card design for our triathlon training company.

Lakeshore Pace Fitness is an Australian business, owned by women, run for women. Lakeshore Pace Fitness helps women prepare or improve triathlon skills and confidence through triathlon camps completely designed for women.

Our camps focus on preparing women both physically and mentally for their next (or first!) triathlon.

You can see our website www.lakeshorepacefitness.com.au for more info about our business and our style.

We've attached two of our logos and are happy to consider a design that utilised either colour scheme with the teal colour being our 'feature' colour. We don't want overly feminine cards but rather cards that are professional and neat. If the inclusion of any pictures/art is warranted, this should be focused on our swim/ride/run theme and in that specific order (swim/ride/run).

The business card needs to be a printable design and the contact details will need to change for our two employees.

Target Market(s)

Female clients and partners/vendors/sponsors that we work with in the triathlon industry

Industry/Entity Type

Fitness

Contact Information for Business Card

Lakeshore Pace Fitness (business name)
Maren Dunley
Business Director
Mobile: 0455 918 237
Email: maren@lakeshorepacefitness.com.au
www.lakeshorepacefitness.com.au

Second business card:
Lakeshore Pace Fitness
Bea Calvert
Coaching Director
Mobile: 0433 206 519
Email: bea@lakeshorepacefitness.com.au

Font styles to use
Serif
Sans Serif

Requirements
Must have
• Core contact details above, our logo and be a printable design
Should not have
• Pink
• Cursive/script fonts

```html
<!DOCTYPE html>
<html lang="en">
<head>
<meta charset="utf-8">
<title>Lakeshore Pace Fitness — Business Cards</title>
<link rel="stylesheet" href="https://fonts.googleapis.com/css2?family=Open+Sans:wght@400;600;700&display=swap">
<style>
  :root {
    --teal: #1aa5b8;
    --slate: #5f6b72;
    --ink: #222a2e;
    --rule: #7a848a;
    --card: #ffffff;
    --backdrop: #e7e9ea;
  }
  * { box-sizing: border-box; margin: 0; padding: 0; }
  html, body {
    width: 1200px; height: 768px; overflow: hidden;
    background: var(--backdrop);
    font-family: "Open Sans", Arial, sans-serif;
  }
  .stage {
    position: relative; width: 1200px; height: 768px;
    display: flex; align-items: center; justify-content: center; gap: 60px;
  }
  .card {
    position: relative; width: 510px; height: 312px;
    background: var(--card);
    box-shadow: 0 6px 18px rgba(0,0,0,0.14);
  }

  /* Front */
  .card-front { display: flex; flex-direction: column; align-items: center; justify-content: center; }
  .brand-name {
    color: var(--teal); font-weight: 700; letter-spacing: 0.5px;
    text-transform: uppercase; line-height: 1.05; text-align: center;
  }
  .card-front .brand-name { font-size: 34px; }
  .brand-dot {
    display: inline-block; width: 14px; height: 14px; border-radius: 50%;
    background: var(--teal); margin-bottom: 14px;
  }
  .front-web {
    display: flex; align-items: center; gap: 14px; margin-top: 40px;
    color: var(--slate); font-size: 13px; font-weight: 600;
  }
  .front-web .accent { width: 70px; height: 2px; background: var(--teal); }

  /* Back */
  .card-back .brand-name {
    position: absolute; right: 34px; top: 58px; font-size: 22px; text-align: right;
  }
  .person { position: absolute; left: 34px; top: 112px; }
  .person-name { color: var(--teal); font-weight: 700; font-size: 19px; letter-spacing: 0.6px; }
  .person-role { color: var(--ink); font-size: 11.5px; margin-top: 1px; }
  .divider {
    position: absolute; left: 210px; right: 34px; top: 166px;
    height: 1.5px; background: var(--rule);
  }
  .contacts { position: absolute; left: 34px; top: 178px; list-style: none; }
  .contacts li {
    display: flex; align-items: center; gap: 10px;
    color: var(--ink); font-size: 12.5px; line-height: 21px;
  }
  .contacts svg { width: 11px; height: 11px; fill: var(--teal); flex: none; }
</style>
</head>
<body>
<main class="stage">

  <section class="card card-front" aria-label="Business card front">
    <span class="brand-dot"></span>
    <div class="brand-name">Lakeshore Pace<br>Fitness</div>
    <div class="front-web">
      <span class="accent"></span>
      <span>www.lakeshorepacefitness.com.au</span>
      <span class="accent"></span>
    </div>
  </section>

  <section class="card card-back" aria-label="Business card back">
    <div class="brand-name">Lakeshore Pace<br>Fitness</div>
    <div class="person">
      <div class="person-name">MAREN DUNLEY</div>
      <div class="person-role">Business Director</div>
    </div>
    <div class="divider"></div>
    <ul class="contacts">
      <li>
        <svg viewBox="0 0 24 24" aria-hidden="true"><path d="M6.6 10.8a15.1 15.1 0 0 0 6.6 6.6l2.2-2.2a1 1 0 0 1 1-.25 11.4 11.4 0 0 0 3.6.57 1 1 0 0 1 1 1V20a1 1 0 0 1-1 1A17 17 0 0 1 3 4a1 1 0 0 1 1-1h3.5a1 1 0 0 1 1 1c0 1.25.2 2.45.57 3.57a1 1 0 0 1-.25 1z"/></svg>
        <span>0455 918 237</span>
      </li>
      <li>
        <svg viewBox="0 0 24 24" aria-hidden="true"><path d="M2 5h20v14H2z M2 5l10 8 10-8" stroke="#fff" stroke-width="1.5"/></svg>
        <span>maren@lakeshorepacefitness.com.au</span>
      </li>
      <li>
        <svg viewBox="0 0 24 24" aria-hidden="true"><circle cx="12" cy="12" r="10"/><path d="M2 12h20M12 2c3 3 3 17 0 20M12 2c-3 3-3 17 0 20" stroke="#fff" stroke-width="1.4" fill="none"/></svg>
        <span>www.lakeshorepacefitness.com.au</span>
      </li>
    </ul>
  </section>

</main>
</body>
</html>
```